Modern Label for Loose Tea pouches on 4.5x6 Label

We need a new label for our teas that is very simple in design, but stylish and modern. This will be used to print labels for our loose tea pouches. The label will be at max 4.5x6 inches in size. There should be a place for the tea name, description, ingredients, and size that is changeable.
Preferably an AI file that allows me to setup variables to change the above items. There will also need to be our logo which is supplied, and our address on the label.
Address:
Brevo Leaf
846 Lower Maple Lane
Cedar Falls, VT 05617
Target Market(s)
Tea Lovers
Requirements
Must have
- Adobe Illustrator file with variables setup for replacement of tea name, description, ingredients, and size (weights 2oz, 4oz, 8oz, 1lb)

```html
<!DOCTYPE html>
<html lang="en">
<head>
<meta charset="utf-8">
<title>Acai Berry White – Brevo Leaf Tea Label</title>
<link href="https://fonts.googleapis.com/css2?family=Lobster&family=Oswald:wght@600&family=Source+Sans+3:wght@400;700&display=swap" rel="stylesheet">
<style>
  :root {
    --teal: #1aa597;
    --teal-deep: #12a89b;
    --ink: #151515;
    --white: #ffffff;
    --shadow-grey: #8a8a8e;
    --title-shadow: #3a3a3a;
  }
  * { margin: 0; padding: 0; box-sizing: border-box; }
  html, body { width: 900px; height: 1200px; overflow: hidden; background: var(--white); }
  .label {
    position: relative;
    width: 900px;
    height: 1200px;
    font-family: "Source Sans 3", "Myriad Pro", sans-serif;
  }
  .brand-panel {
    position: absolute;
    left: 207px; top: 0;
    width: 471px; height: 261px;
    background: var(--teal);
  }
  .brand-mark {
    position: absolute;
    left: 50%; top: 62px;
    width: 64px; height: 64px;
    margin-left: -32px;
    border: 4px solid var(--white);
    border-radius: 50%;
  }
  .brand-name {
    position: absolute;
    left: 0; right: 0; top: 166px;
    text-align: center;
    color: var(--white);
    font-weight: 700;
    font-size: 46px;
    letter-spacing: 1px;
  }
  .body-panel {
    position: absolute;
    left: 71px; top: 392px;
    width: 747px; height: 762px;
    background: var(--teal);
    border-radius: 0 0 34px 34px;
  }
  .title-banner {
    position: absolute;
    left: 68px; top: 270px;
    width: 757px; height: 124px;
    background: var(--teal-deep);
    border-radius: 14px;
    border-bottom: 6px solid var(--white);
  }
  .tea-name {
    position: absolute;
    left: 0; right: 0; top: 2px;
    text-align: center;
    font-family: "Lobster", cursive;
    font-weight: 400;
    font-size: 97px;
    color: var(--white);
    text-shadow: 4px 4px 0 var(--title-shadow);
    white-space: nowrap;
  }
  .chevron {
    position: absolute;
    left: 198px; top: 396px;
  }
  .description {
    position: absolute;
    left: 138px; top: 543px;
    font-size: 26px;
    line-height: 33.6px;
    color: var(--ink);
    white-space: nowrap;
  }
  .ingredients {
    position: absolute;
    left: 164px; top: 738px;
    font-size: 27.5px;
    line-height: 33.6px;
    color: var(--white);
    white-space: nowrap;
  }
  .line { display: block; }
  .ingredients strong { font-weight: 700; font-size: 29px; }
  .net-weight {
    position: absolute;
    left: 71px; width: 747px; top: 908px;
    text-align: center;
    color: var(--ink);
    font-size: 31px;
    font-weight: 700;
    font-family: Arial, "Helvetica Neue", sans-serif;
  }
  .net-weight .net-label {
    font-family: "Oswald", sans-serif;
    font-weight: 600;
    font-size: 29px;
    letter-spacing: -1px;
    margin-right: 2px;
  }
  .address {
    position: absolute;
    left: 71px; width: 747px; top: 1010px;
    text-align: center;
    color: var(--white);
    font-size: 21.5px;
    white-space: nowrap;
  }
</style>
</head>
<body>
<div class="label">
  <div class="brand-panel">
    <div class="brand-mark"></div>
    <div class="brand-name">Brevo Leaf</div>
  </div>

  <div class="body-panel"></div>

  <svg class="chevron" width="492" height="130" viewBox="0 0 492 130" aria-hidden="true">
    <polyline points="8,0 8,52 244,118 480,52 480,0" fill="none" stroke="var(--shadow-grey)" stroke-width="8" transform="translate(0,6)"/>
    <polyline points="8,0 8,48 244,114 480,48 480,0" fill="none" stroke="var(--white)" stroke-width="8"/>
  </svg>

  <div class="title-banner">
    <h1 class="tea-name">Acai Berry White</h1>
  </div>

  <p class="description">
    <span class="line">Delicious and good for you. This loose leaf white tea</span>
    <span class="line">blend features “super food” acai mixed delicately with</span>
    <span class="line">exotic, flavorful berries to create a deliciously flavorful</span>
    <span class="line">white tea blend packed with antioxidants.</span>
  </p>

  <p class="ingredients">
    <span class="line"><strong>INGREDIENTS</strong>: White tea scented with natural</span>
    <span class="line">Acai berry and sprinkled with blue corn flowers.</span>
  </p>

  <p class="net-weight"><span class="net-label">NET WT</span> 1lb(454g)</p>

  <p class="address">ADDRESS: Brevo Leaf | 846 Lower Maple Lane | Cedar Falls, VT 05617</p>
</div>
</body>
</html>
```